KVRo Business Cards

We need a business card design. We are a Technology (Audio Visual) design, sales and installation company. Looking for a double sided design, clean

Contact Information for Business Card

Clean, modern look, 2 sided

Font styles to use
Sans Serif

```html
<!DOCTYPE html>
<html lang="en">
<head>
<meta charset="utf-8">
<title>KVRo Business Cards</title>
<link href="https://fonts.googleapis.com/css2?family=Open+Sans:wght@400;600;800&display=swap" rel="stylesheet">
<style>
  :root {
    --navy: #1c2b3a;
    --orange: #f7941d;
    --grey-text: #5a6470;
    --divider: #8a939c;
    --paper: #ffffff;
    --backdrop: #d9d9d6;
  }
  * { box-sizing: border-box; margin: 0; padding: 0; }
  html, body {
    width: 1200px;
    height: 801px;
    overflow: hidden;
  }
  body {
    background: var(--backdrop);
    font-family: "Open Sans", Arial, sans-serif;
    position: relative;
  }
  .card {
    position: absolute;
    top: 246px;
    width: 540px;
    height: 309px;
    box-shadow: 0 6px 18px rgba(0,0,0,0.12);
  }
  .card-front {
    left: 40px;
    background: var(--paper);
  }
  .card-back {
    left: 620px;
    background: var(--orange);
  }
  .front-wordmark {
    position: absolute;
    left: 34px;
    top: 50%;
    transform: translateY(-50%);
    font-size: 82px;
    font-weight: 800;
    letter-spacing: -1px;
    color: var(--navy);
    line-height: 1;
  }
  .front-divider {
    position: absolute;
    left: 280px;
    top: 70px;
    width: 1px;
    height: 170px;
    background: var(--divider);
  }
  .contact-block {
    position: absolute;
    left: 298px;
    top: 78px;
    color: var(--grey-text);
    font-size: 13px;
    line-height: 1.45;
  }
  .contact-name {
    font-size: 19px;
    font-weight: 800;
    color: var(--navy);
    letter-spacing: 0.3px;
    line-height: 1.2;
  }
  .contact-title {
    margin-bottom: 10px;
  }
  .contact-address {
    margin-bottom: 10px;
  }
  .contact-line {
    display: flex;
    align-items: center;
    gap: 7px;
  }
  .contact-icon {
    width: 11px;
    height: 11px;
    flex: none;
  }
  .back-wordmark {
    position: absolute;
    right: 70px;
    bottom: 92px;
    font-size: 40px;
    font-weight: 800;
    color: var(--paper);
    letter-spacing: -0.5px;
    line-height: 1;
  }
</style>
</head>
<body>
  <section class="card card-front" aria-label="Card front">
    <div class="front-wordmark">KVRo</div>
    <div class="front-divider"></div>
    <div class="contact-block">
      <div class="contact-name">DANA WHITLOCK</div>
      <div class="contact-title">President</div>
      <div class="contact-address">1180 Harbor Crest Way<br>Bayview CA 90412</div>
      <div class="contact-line">
        <svg class="contact-icon" viewBox="0 0 12 12" aria-hidden="true">
          <circle cx="6" cy="6" r="6" fill="var(--orange)"/>
          <path d="M3.6 3.2 L5 3 L5.5 4.6 L4.7 5.2 Q5.4 6.7 6.8 7.3 L7.4 6.5 L9 7 L8.8 8.4 Q5 8.6 3.6 3.2 Z" fill="#fff"/>
        </svg>
        <span>555-014-2287</span>
      </div>
      <div class="contact-line">
        <svg class="contact-icon" viewBox="0 0 12 12" aria-hidden="true">
          <rect x="0.5" y="2" width="11" height="8" rx="1" fill="var(--orange)"/>
          <path d="M1 2.5 L6 6.5 L11 2.5" fill="none" stroke="#fff" stroke-width="1"/>
        </svg>
        <span>danawhitlock@kvro.com</span>
      </div>
      <div class="contact-line">
        <svg class="contact-icon" viewBox="0 0 12 12" aria-hidden="true">
          <circle cx="6" cy="6" r="6" fill="var(--orange)"/>
          <ellipse cx="6" cy="6" rx="2.4" ry="5" fill="none" stroke="#fff" stroke-width="0.9"/>
          <line x1="1" y1="6" x2="11" y2="6" stroke="#fff" stroke-width="0.9"/>
        </svg>
        <span>www.kvro.com</span>
      </div>
    </div>
  </section>

  <section class="card card-back" aria-label="Card back">
    <div class="back-wordmark">KVRo</div>
  </section>
</body>
</html>
```